Yoga Training Cerificate

Design a certificate of graduation from a Vinyasa Yoga Teacher Training Program.

The attached document is an example of the certificate I received as a graduate from a teacher training program. You can use it as a template.

Stylistically, what you design can be: visually enticing, professional, clean, and modern.

Please develop the "Tidal Lotus" logo and embed it within the certificate.

Please add a circular watermark behind the body of the certificate similar to the one found in the attachment; leave out the words Asana Guild because I am not associated with that organization.

The name of my school is "Tidal Lotus." And it was established in 2017, which you can include.

The certificate affirms that "' 'such-and-such' has successfully completed the Tidal Lotus modern vinyasa yoga training, completing two hundred hours of instruction in practice and theory. Within the power of our institution as a certifying agent we declare Such-and-such, now, a teacher competent to share the gift of yoga with the masses in a safe and effective."

My name -Dennis Halvorsen- should be at bottom with a faux-signature; position title: Tidal Lotus founder.

If you decide to include text on the fringe, like the example, it might include bars of text describing the maxims of the Tidal Lotus school reading:

This is Tidal Lotus
Breath is primary
Evolve the physical culture
Bring your unique expression to the practice
Take Breaks
Freestyle
Close your eyes
Feel deeper into your body
This is active meditation
This is moving meditation
This is modern meditation

And find a way to integrate Emojis like: Fire, Water, Prayer Hands, etc. as you see fit.

Generally, make the certificate look: official, clear and clean. You can base it from the example given. And try and create a graphic design that is more visually capturing then the example.

```html
<!DOCTYPE html>
<html lang="en">
<head>
<meta charset="utf-8">
<title>Tidal Lotus — Certificate of Completion</title>
<link href="https://fonts.googleapis.com/css2?family=Great+Vibes&family=Raleway:wght@300&family=Roboto:wght@300;400;700&family=Roboto+Condensed:wght@400;700&display=swap" rel="stylesheet">
<style>
  :root {
    --paper: #ffffff;
    --ink: #231f20;
    --ink-soft: #5a5a5a;
    --brand-grey: #6d6d6d;
    --seal: #dcdcdc;
    --rule: #2b2b2b;
  }
  * { margin: 0; padding: 0; box-sizing: border-box; }
  html, body { width: 1200px; height: 849px; overflow: hidden; background: var(--paper); }
  .certificate { position: relative; width: 1200px; height: 849px; background: var(--paper); color: var(--ink); font-family: "Roboto", Arial, sans-serif; }

  .maxims { position: absolute; left: 78px; top: 122px; list-style: none; }
  .maxims li { font-family: "Raleway", Arial, sans-serif; font-weight: 300; font-size: 16px; color: var(--ink-soft); height: 46.6px; line-height: 24px; }

  .brand { position: absolute; left: 96px; top: 646px; display: flex; align-items: center; gap: 18px; }
  .brand-dot { width: 50px; height: 50px; border-radius: 50%; background: var(--brand-grey); }
  .brand-name { font-family: "Raleway", Arial, sans-serif; font-weight: 300; font-size: 52px; color: var(--brand-grey); letter-spacing: -0.5px; }

  .divider { position: absolute; left: 481px; top: 108px; width: 2px; height: 632px; background: var(--ink-soft); }

  .seal { position: absolute; left: 590px; top: 138px; }

  .body { position: absolute; left: 500px; width: 676px; text-align: center; }
  .title { top: 144px; font-family: "Great Vibes", cursive; font-size: 66px; line-height: 80px; font-weight: 400; }
  .affirms { top: 233px; font-weight: 300; font-size: 18px; }
  .recipient { top: 268px; font-weight: 700; font-size: 66px; line-height: 80px; letter-spacing: 0.5px; }
  .statement { top: 360px; font-weight: 300; font-size: 22px; line-height: 28.5px; }
  .declaration { top: 484px; font-weight: 300; font-size: 22px; line-height: 28.5px; }
  .declaration strong { font-weight: 700; }

  .signature { position: absolute; top: 666px; text-align: center; }
  .signature .rule { height: 3px; background: var(--rule); margin-bottom: 8px; }
  .signature .name { font-family: "Roboto Condensed", Arial, sans-serif; font-weight: 700; font-size: 25px; line-height: 28px; }
  .signature .role { font-weight: 300; font-size: 21px; line-height: 28px; }
  .founder { left: 518px; width: 264px; }
  .date { left: 986px; width: 140px; }
</style>
</head>
<body>
<main class="certificate">
  <ul class="maxims">
    <li>This is Tidal Lotus</li>
    <li>Breath is primary</li>
    <li>Evolve the physical culture</li>
    <li>Bring your unique expression to the practice</li>
    <li>Take Breaks</li>
    <li>Freestyle</li>
    <li>Close your eyes</li>
    <li>Feel deeper into your body</li>
    <li>This is active meditation</li>
    <li>This is moving meditation</li>
    <li>This is modern meditation</li>
  </ul>

  <div class="brand">
    <span class="brand-dot"></span>
    <span class="brand-name">Tidal Lotus</span>
  </div>

  <div class="divider"></div>

  <svg class="seal" width="496" height="496" viewBox="0 0 496 496" aria-hidden="true">
    <circle cx="248" cy="248" r="228" fill="none" stroke="var(--seal)" stroke-width="22"/>
  </svg>

  <h1 class="body title">Certificate of Completion</h1>
  <p class="body affirms">The certificate affirms that</p>
  <p class="body recipient">MARA ELLISON</p>
  <p class="body statement">has successfully completed<br>The Tidal Lotus modern vinyasa yoga training<br>completing two hundred hours of<br>instruction in practice and theory.</p>
  <p class="body declaration">Within the power of our institution as a certifying agent<br>we declare <strong>MARA ELLISON</strong>, now, a teacher<br>competent to share the gift of yoga<br>with the masses in a safe and effective manner.</p>

  <div class="signature founder">
    <div class="rule"></div>
    <div class="name">DENNIS HALVORSEN</div>
    <div class="role">TIDAL LOTUS FOUNDER</div>
  </div>
  <div class="signature date">
    <div class="rule"></div>
    <div class="name">DATE</div>
  </div>
</main>
</body>
</html>
```